Print and E-book Personal Injury Front and Back Book Cover

I need a book cover for a personal injury law firm book titled "Rising Past the Wreckage" with the subtitle "A Plain Guide for Harmed Readers." The book cover should have an image. This isas a lead generation book designed to be give to potential clients to have them sign as new clients.

Target Market(s)

Potential New Clients Looking For a Personal Injury Attorney

Industry/Entity Type

Legal

Requirements
Must have
• Title and some type of image or images

```html
<!DOCTYPE html>
<html lang="en">
<head>
<meta charset="utf-8">
<title>Rising Past the Wreckage — Cover</title>
<link href="https://fonts.googleapis.com/css2?family=Cinzel:wght@400;500&display=swap" rel="stylesheet">
<style>
  :root {
    --backdrop: #e6e6e6;
    --cover: #151515;
    --spine: #1b1b1b;
    --ink-light: #f2eee8;
    --accent: #e3d3bf;
    --accent-ink: #2a2118;
    --rule: #b89f82;
    --shelf-warm: #8a5a30;
    --shelf-mid: #5a3a22;
    --shelf-dark: #1e2433;
    --marble: #d9d4cc;
    --paper: #d8ccc0;
    --paper-shade: #6e5f55;
    --mark: #6a6a6a;
  }
  html, body {
    margin: 0;
    width: 1200px;
    height: 927px;
    overflow: hidden;
    background: var(--backdrop);
  }
  .book {
    position: absolute;
    left: 255px;
    top: 28px;
    width: 690px;
    height: 870px;
    display: flex;
    box-shadow: 0 14px 40px rgba(0,0,0,0.25);
    font-family: "Cinzel", serif;
    color: var(--ink-light);
  }

  /* Spine */
  .spine {
    position: relative;
    width: 110px;
    height: 100%;
    background: var(--spine);
    border-right: 1px solid #2a2a2a;
    overflow: hidden;
  }
  .spine-photo {
    position: absolute;
    left: 0; bottom: 0;
    width: 100%;
    height: 200px;
    background: linear-gradient(180deg, var(--spine) 0%, #2c2622 55%, #4a3f38 100%);
  }
  .spine-title {
    position: absolute;
    left: 50%;
    top: 120px;
    transform: translateX(-50%);
    writing-mode: vertical-rl;
    font-size: 27px;
    letter-spacing: 2px;
    white-space: nowrap;
  }
  .spine-imprint {
    position: absolute;
    left: 50%;
    bottom: 34px;
    transform: translateX(-50%);
    writing-mode: vertical-rl;
    display: flex;
    align-items: center;
    gap: 8px;
    font-size: 12px;
    color: var(--accent);
    white-space: nowrap;
  }
  .spine-imprint-dot {
    width: 12px; height: 12px;
    border-radius: 50%;
    background: var(--accent);
  }

  /* Front cover */
  .cover {
    position: relative;
    width: 580px;
    height: 100%;
    background: var(--cover);
    overflow: hidden;
  }
  .shelf-photo {
    position: absolute;
    left: 250px; top: 0;
    width: 330px;
    height: 300px;
    background:
      repeating-linear-gradient(180deg, transparent 0 64px, #0e0e0e 64px 72px),
      linear-gradient(90deg, var(--shelf-mid) 0%, var(--shelf-warm) 45%, #a06c3c 70%, var(--shelf-dark) 100%);
    -webkit-mask-image: linear-gradient(180deg, #000 0%, #000 70%, transparent 100%);
            mask-image: linear-gradient(180deg, #000 0%, #000 70%, transparent 100%);
  }
  .hall-photo {
    position: absolute;
    left: 0; top: 60px;
    width: 250px;
    height: 280px;
    background:
      linear-gradient(160deg, transparent 30%, rgba(217,212,204,0.75) 55%, rgba(217,212,204,0.35) 75%, transparent 92%),
      linear-gradient(180deg, var(--shelf-dark) 0%, #141519 100%);
    -webkit-mask-image: linear-gradient(180deg, #000 0%, #000 75%, transparent 100%);
            mask-image: linear-gradient(180deg, #000 0%, #000 75%, transparent 100%);
  }
  .writing-photo {
    position: absolute;
    left: 0; bottom: 0;
    width: 100%;
    height: 210px;
    background:
      linear-gradient(180deg, var(--cover) 0%, transparent 35%),
      linear-gradient(90deg, var(--paper) 0%, #bfb1a4 45%, var(--paper-shade) 75%, #2e2622 100%);
  }

  .title-block {
    position: absolute;
    left: 0; top: 350px;
    width: 100%;
    text-align: center;
  }
  .title-small {
    display: inline-block;
    background: var(--accent);
    color: var(--accent-ink);
    font-size: 22px;
    padding: 2px 8px 0;
    line-height: 1.1;
  }
  .title-large {
    display: block;
    font-size: 60px;
    line-height: 1;
    letter-spacing: 1px;
  }
  .title-joiner {
    display: inline-block;
    width: 34px; height: 34px;
    border-radius: 50%;
    background: var(--accent);
    color: var(--accent-ink);
    font-size: 14px;
    line-height: 34px;
    margin: 4px 0;
  }
  .publisher {
    position: absolute;
    right: 26px;
    top: 576px;
    font-size: 11px;
    color: var(--mark);
    display: flex;
    align-items: center;
    gap: 6px;
  }
  .publisher-dot {
    width: 8px; height: 8px;
    border-radius: 50%;
    background: var(--mark);
  }
  .subtitle {
    position: absolute;
    left: 40px; right: 40px;
    top: 604px;
    border-top: 1px solid var(--rule);
    border-bottom: 1px solid var(--rule);
    padding: 8px 0;
    text-align: center;
    font-size: 17px;
    letter-spacing: 1px;
  }
</style>
</head>
<body>
  <div class="book">
    <div class="spine">
      <div class="spine-photo" role="img" aria-label="Edge of a sheet of paper in warm low light"></div>
      <div class="spine-title">Rising Past the Wreckage</div>
      <div class="spine-imprint"><span class="spine-imprint-dot"></span>Larkspur</div>
    </div>

    <div class="cover">
      <div class="shelf-photo" role="img" aria-label="Tall library shelves of old leather-bound books"></div>
      <div class="hall-photo" role="img" aria-label="Dim library hall with a row of white marble busts"></div>
      <div class="writing-photo" role="img" aria-label="Fountain pen writing on a sheet of paper in warm low light"></div>

      <div class="title-block">
        <span class="title-small">Rising</span>
        <span class="title-large">Past</span>
        <span class="title-joiner">the</span>
        <span class="title-large">Wreckage</span>
      </div>

      <div class="publisher"><span class="publisher-dot"></span>Larkspur Books</div>

      <div class="subtitle">A Plain Guide for Harmed Readers</div>
    </div>
  </div>
</body>
</html>
```